Tots at Play

We need a logo and graphich design for a one page text for our Tots @play program, it would nened to match or be inspired from our corporate indentity which can be seen at www.halvora-partners.com

Dear XXX
BRT is proud to launch its first ever TOTS @ PLAY day! We invite you and your child(ren) to join us on this special day, and strengthen the connection between education and work, and your relationship between parent and child(ren).

Who? All children, all ages
Where? BRT offices
When? January 29th, from 13h – 17h

Tots @ Play is the perfect time to start shaping your children’s future through education and experience at BRT with a program tailored to target each age group. There will be group activities and sessions, as well as one on one time for parents and their children.
We are excited to work together with you and your children to create a true sense of community, and celebrate the opportunities and possibilities for the next generation. It’s a day to share your passion and know-how and show what happens when you are at work. We will show children the value of education and help them discover the power and potential of a balanced work and family life. We would like to give you and your children an opportunity to express their future goals and dreams and help begin together the steps towards achieving these through the follow up with Tots @ Quest. BRT is developing a multi-program to enable parents and children to realize the future they dream of.
We look forward to seeing you @ Work!

Industry/Entity Type

Education

```html
<!DOCTYPE html>
<html lang="en">
<head>
<meta charset="utf-8">
<title>Tots @ Play – Invitation</title>
<link rel="stylesheet" href="https://fonts.googleapis.com/css2?family=Exo+2:wght@400;500;700&display=swap">
<style>
  :root {
    --berry: #c0335f;
    --berry-deep: #b02a55;
    --ink: #2e2540;
    --paper: #ffffff;
    --photo-light: #f3efe9;
    --photo-warm: #d9c4a8;
  }
  * { margin: 0; padding: 0; box-sizing: border-box; }
  html, body { width: 852px; height: 1200px; overflow: hidden; background: var(--paper); }
  body { font-family: "Exo 2", sans-serif; color: var(--paper); }

  .flyer { position: relative; width: 852px; height: 1200px; overflow: hidden; }

  .hero { position: absolute; left: 0; top: 0; width: 852px; height: 521px; }
  .hero-photo {
    position: absolute; inset: 0;
    background: linear-gradient(120deg, var(--photo-light) 0%, #eadfd2 35%, var(--photo-warm) 60%, #e8e4e0 100%);
  }
  .hero-curve { position: absolute; inset: 0; }
  .brand {
    position: absolute; left: 366px; top: 38px;
    font-weight: 700; font-size: 64px; letter-spacing: -1px;
    color: var(--berry); white-space: nowrap;
  }

  .letter {
    position: absolute; left: 0; top: 530px; width: 852px; height: 670px;
    background: linear-gradient(180deg, var(--berry) 0%, var(--berry-deep) 100%);
    padding: 8px 58px 0 58px;
  }
  .greeting { font-weight: 700; font-size: 21px; margin-bottom: 16px; }
  .copy { font-size: 16.6px; line-height: 24px; text-align: justify; font-weight: 400; }
  .copy strong { font-weight: 700; }
  .copy + .copy { margin-top: 24px; }

  .facts { position: relative; height: 96px; margin: 10px 0 20px; }
  .fact {
    position: absolute; top: 0; height: 94px;
    background: var(--paper); border-radius: 16px; color: var(--ink);
    text-align: center; padding-top: 12px;
  }
  .fact-who { left: 25px; width: 207px; }
  .fact-where { left: 242px; width: 181px; }
  .fact-when { left: 434px; width: 271px; }
  .fact-title { font-weight: 700; font-size: 35px; line-height: 38px; }
  .fact-detail { font-weight: 500; font-size: 16.5px; margin-top: 6px; }

  .signoff { font-size: 23px; margin-top: 20px; }
  .signoff strong { font-weight: 700; }
</style>
</head>
<body>
<div class="flyer">
  <header class="hero">
    <div class="hero-photo" role="img" aria-label="Photo of a parent and two children smiling at a computer keyboard"></div>
    <svg class="hero-curve" width="852" height="521" viewBox="0 0 852 521" aria-hidden="true">
      <path d="M596,0 C770,70 800,330 464,521 L852,521 L852,0 Z" fill="var(--ink)"/>
    </svg>
    <div class="brand">Tots @ Play</div>
  </header>

  <main class="letter">
    <p class="greeting">Dear XXX</p>
    <p class="copy">BRT is proud to launch its first ever <strong>TOTS @ PLAY</strong> day! We invite you and your child(ren) to join us on this special day, and strengthen the connection between education and work, and your relationship between parent and child(ren).</p>

    <section class="facts">
      <div class="fact fact-who"><div class="fact-title">Who?</div><div class="fact-detail">All children, all ages</div></div>
      <div class="fact fact-where"><div class="fact-title">Where?</div><div class="fact-detail">BRT offices</div></div>
      <div class="fact fact-when"><div class="fact-title">When?</div><div class="fact-detail">January 29th, from 13h – 17h</div></div>
    </section>

    <p class="copy"><strong>Tots @ Play</strong> is the perfect time to start shaping your children’s future through education and experience at BRT with a program tailored to target each age group. There will be group activities and sessions, as well as one on one time for parents and their children.</p>
    <p class="copy">We are excited to work together with you and your children to create a true sense of community, and celebrate the opportunities and possibilities for the next generation. It’s a day to share your passion and know-how and show what happens when you are at work. We will show children the value of education and help them discover the power and potential of a balanced work and family life. We would like to give you and your children an opportunity to express their future goals and dreams and help begin together the steps towards achieving these through the follow up with <strong>Tots @ Quest</strong>. BRT is developing a multi-program to enable parents and children to realize the future they dream of.</p>

    <p class="signoff">We look forward to seeing you <strong>@ Work</strong>!</p>
  </main>
</div>
</body>
</html>
```